Home Staging Company needs business card design

We're a home staging company called Brightly Settled Home Staging. We would like a business card design that includes aqua and gray. Our current logo of house within chair is fine but I find we almost always use the logo in one color. I'll upload images of front and back of our current card and our logo. Note that we have dropped "Solutions" from our company name and don't want to include it on the card.

Target Market(s)

Realtors and homeowners - people interested in selling their homes

Contact Information for Business Card

Marisol Vantrease
Brightly Settled Home Staging
612-348-9071
www.brightlysettled.example
marisol@brightlysettled.example

Font styles to use
Serif
Script

Requirements
Must have
• My logo and contact details
• UPDATE***
• I forgot to say that the company name should be included on the front of the card somehow.

```html
<!DOCTYPE html>
<html lang="en">
<head>
<meta charset="utf-8">
<title>Brightly Settled Home Staging — Business Card</title>
<link rel="stylesheet" href="https://fonts.googleapis.com/css2?family=Playfair+Display:wght@400;700&family=Roboto:wght@400&display=swap">
<style>
  :root {
    --backdrop: #111111;
    --charcoal: #3b3b3d;
    --charcoal-tone: #444446;
    --paper: #ffffff;
    --paper-tone: #f3f3f3;
    --ink: #2b2b2b;
    --aqua: #5ec6c4;
    --white: #ffffff;
  }
  * { box-sizing: border-box; margin: 0; padding: 0; }
  html, body {
    width: 1200px;
    height: 1000px;
    overflow: hidden;
    background: var(--backdrop);
  }
  .sheet {
    position: relative;
    width: 1200px;
    height: 1000px;
    display: flex;
    align-items: center;
    justify-content: center;
    gap: 50px;
  }
  .card {
    position: relative;
    width: 525px;
    height: 300px;
    overflow: hidden;
    border-radius: 3px;
  }
  .card-texture {
    position: absolute;
    inset: 0;
  }

  /* Front */
  .card-front { background: var(--charcoal); }
  .card-front .card-texture { background: var(--charcoal-tone); opacity: 0.35; }
  .brand {
    position: absolute;
    inset: 0;
    display: flex;
    flex-direction: column;
    align-items: center;
    justify-content: center;
    color: var(--white);
    font-family: "Playfair Display", serif;
    font-weight: 400;
  }
  .brand-dot {
    width: 44px;
    height: 44px;
    border-radius: 50%;
    background: var(--white);
    margin-bottom: 16px;
  }
  .brand-name { font-size: 38px; line-height: 1.1; }
  .brand-tagline {
    margin-top: 6px;
    font-size: 12px;
    letter-spacing: 3px;
    text-transform: uppercase;
  }

  /* Back */
  .card-back { background: var(--paper); }
  .card-back .card-texture { background: var(--paper-tone); opacity: 0.5; }
  .accent {
    position: absolute;
    width: 32px;
    height: 34px;
  }
  .accent-left { left: 0; top: 118px; }
  .accent-right { right: 0; top: 165px; }
  .holder-name {
    position: absolute;
    top: 42px;
    right: 38px;
    font-family: "Playfair Display", serif;
    font-weight: 700;
    font-size: 34px;
    color: var(--ink);
  }
  .back-brand {
    position: absolute;
    top: 120px;
    left: 0;
    right: 0;
    display: flex;
    align-items: center;
    justify-content: center;
    gap: 8px;
    font-family: "Roboto", sans-serif;
    font-size: 15px;
    color: var(--ink);
  }
  .back-brand-dot {
    width: 22px;
    height: 22px;
    border-radius: 50%;
    background: var(--ink);
  }
  .contact {
    position: absolute;
    left: 44px;
    bottom: 42px;
    font-family: "Roboto", sans-serif;
    font-size: 17px;
    line-height: 1.45;
    color: var(--ink);
  }
  .contact-line-web { padding-left: 40px; }
</style>
</head>
<body>
<main class="sheet">
  <section class="card card-front" aria-label="Business card front">
    <div class="card-texture" role="img" aria-label="Subtle diamond lattice pattern"></div>
    <div class="brand">
      <span class="brand-dot"></span>
      <span class="brand-name">Brightly Settled</span>
      <span class="brand-tagline">Home Staging</span>
    </div>
  </section>

  <section class="card card-back" aria-label="Business card back">
    <div class="card-texture" role="img" aria-label="Subtle diamond lattice pattern"></div>
    <svg class="accent accent-left" viewBox="0 0 32 34" aria-hidden="true">
      <polygon points="0,0 32,34 0,34" fill="var(--aqua)"/>
    </svg>
    <svg class="accent accent-right" viewBox="0 0 32 34" aria-hidden="true">
      <polygon points="32,0 32,34 0,34" fill="var(--aqua)"/>
    </svg>
    <h1 class="holder-name">Marisol Vantrease</h1>
    <div class="back-brand">
      <span class="back-brand-dot"></span>
      <span>Brightly Settled</span>
    </div>
    <address class="contact" style="font-style: normal;">
      <div class="contact-line">612-348-9071 &nbsp;|&nbsp; marisol@brightlysettled.example</div>
      <div class="contact-line contact-line-web">www.brightlysettled.example</div>
    </address>
  </section>
</main>
</body>
</html>
```